Business card: floral shop

I own a flower shop that specializes in Japanese flower settings and weddings. I am looking for a design that has to be colorful, but elegantly simple (unadorned), while implying class, love, and commitment.

My flower shop is also all about outstanding customer service, if this helps at all.

Industry/Entity Type

Floral

Contact Information for Business Card

Company Name: Brightwater Bloom Studio
Name: Marisol Keene
Address: 41 Larkspur Rd, Wexley, MA 01836
Email: petalcrestmail@fernovo.com

Logo Text

Brightwater Bloom Studio

Requirements
Must have
• Flowers, color, company information.

Offer:

"Refer a friend and receive $25 gift certificate at the time of the order"
Should not have
• Black borders

```html
<!DOCTYPE html>
<html lang="en">
<head>
<meta charset="utf-8">
<title>Brightwater Bloom Studio – Business Card</title>
<link rel="stylesheet" href="https://fonts.googleapis.com/css2?family=Pinyon+Script&family=Cinzel:wght@400&family=Source+Sans+3:wght@400&display=swap">
<style>
  :root {
    --backdrop: #2f3032;
    --card-light: #f5f4ee;
    --card-edge: #e2e2d8;
    --ink: #151515;
    --label: #d8806c;
    --tulip: #e3685a;
    --tulip-deep: #c94c42;
    --stem: #8cbf68;
  }
  * { margin: 0; padding: 0; box-sizing: border-box; }
  html, body {
    width: 1200px;
    height: 750px;
    overflow: hidden;
    background: var(--backdrop);
  }
  .canvas {
    position: relative;
    width: 1200px;
    height: 750px;
    display: flex;
    align-items: center;
    justify-content: center;
  }
  .business-card {
    position: relative;
    width: 840px;
    height: 480px;
    background: radial-gradient(ellipse at 45% 50%, var(--card-light) 0%, var(--card-light) 40%, var(--card-edge) 100%);
    overflow: hidden;
  }
  .bouquet {
    position: absolute;
    top: -20px;
    right: -20px;
    width: 330px;
    height: 300px;
    border-bottom-left-radius: 60% 70%;
    border-top-left-radius: 40% 30%;
    background:
      radial-gradient(ellipse at 35% 55%, var(--tulip) 0%, var(--tulip) 40%, rgba(227,104,90,0) 70%),
      linear-gradient(210deg, var(--stem) 0%, var(--stem) 20%, var(--tulip-deep) 55%, var(--tulip) 100%);
  }
  .company-name {
    position: absolute;
    top: 34px;
    left: 58px;
    font-family: "Pinyon Script", cursive;
    font-size: 60px;
    font-weight: 400;
    color: var(--ink);
    white-space: nowrap;
  }
  .person-name {
    position: absolute;
    top: 245px;
    left: 70px;
    font-family: "Cinzel", serif;
    font-size: 40px;
    font-weight: 400;
    letter-spacing: 3px;
    color: var(--ink);
  }
  .contact {
    position: absolute;
    left: 70px;
    bottom: 52px;
    display: grid;
    grid-template-columns: auto auto;
    column-gap: 14px;
    row-gap: 4px;
    font-family: "Source Sans 3", sans-serif;
    font-size: 21px;
    line-height: 1.2;
  }
  .contact dt { color: var(--label); }
  .contact dd { color: var(--ink); }
</style>
</head>
<body>
  <main class="canvas">
    <article class="business-card">
      <div class="bouquet" role="img" aria-label="Bouquet of coral-red tulips with green stems in the top right corner"></div>
      <h1 class="company-name">Brightwater Bloom Studio</h1>
      <p class="person-name">Marisol Keene</p>
      <dl class="contact">
        <dt>Email:</dt>
        <dd>petalcrestmail@fernovo.com</dd>
        <dt>Address:</dt>
        <dd>41 Larkspur Rd, Wexley, MA 01836</dd>
      </dl>
    </article>
  </main>
</body>
</html>
```